Solar for Wineries

I am looking for a 4 page "Renewable Products Brochure" I can used for initial customer contact. My customers are high-end winery owners and wine makers.

Our products are solar electric systems, solar thermal water heating systems and electric vehicle charging systems.

My customers have an high degree of connection to grapes, grape vines, flowing hills of vineyards and beautiful architecture. Green, purple and pastel colors play well.

A key aspect of our selling proposition is that we are a local company. We are their neighbor and their customer. We hire local workers, and bring a serious commitment to the success of our customers.

See our website: www.brantwickpower.com

Logos and pictures uploaded for Solar Winery Project

see posted file for new text content

For those who included the map in you designs, I posted a map with our logo at past installation sites.  Please use my new map, or add the logo at sites as indicated.   I would not add the logos on the map with the grape leaf background.

Thanks.

Brian

Target recipient: male or female, 50-65 years old, college educated, and business savvy. Interests:growing grapes and producing award winning wines.

It Company

• Lots of wine and grape pictures.
A map of the Tilbury Rd area of Plymouth California USA. would promote the idea of a local company.

Need pictures of our solar systems and electric vehicle chargers.
• No tech nuts and bolts pictures. No graphs or formulas.

```html
<!DOCTYPE html>
<html lang="en">
<head>
<meta charset="utf-8">
<title>Solar for Wineries – Brochure Spread</title>
<link rel="stylesheet" href="https://fonts.googleapis.com/css2?family=Arimo:wght@400;700&display=swap">
<style>
  :root {
    --backdrop: #2a2a2a;
    --paper: #ffffff;
    --ink: #3a3a3a;
    --plum: #8b1f7d;
    --sage: #a9b27a;
    --gutter-shade: rgba(0,0,0,0.10);
  }
  * { box-sizing: border-box; margin: 0; padding: 0; }
  html, body {
    width: 1200px; height: 900px; overflow: hidden;
    background: var(--backdrop);
    font-family: "Arimo", Arial, sans-serif;
    color: var(--ink);
  }
  .spread {
    position: absolute; left: 50px; top: 70px;
    width: 1100px; height: 760px;
    display: flex;
    box-shadow: 0 12px 40px rgba(0,0,0,0.5);
  }
  .page {
    position: relative; width: 550px; height: 760px;
    background: var(--paper); overflow: hidden;
  }
  .page--left { box-shadow: inset -18px 0 22px -14px var(--gutter-shade); }
  .page--right { box-shadow: inset 18px 0 22px -14px var(--gutter-shade); }

  .photo { position: absolute; }
  .photo--wine-glasses {
    left: 0; top: 0; width: 550px; height: 290px;
    background: radial-gradient(ellipse at 30% 45%, #e8dfb8 0%, #a7a45a 30%, #5d6a2c 60%, #2f3a18 100%);
  }
  .photo--grapes {
    left: 285px; top: 560px; width: 250px; height: 185px;
    background: radial-gradient(ellipse at 40% 50%, #6b6aa8 0%, #3f3b78 45%, #2f4a22 80%, #5f7a38 100%);
  }
  .photo--collector {
    left: 300px; top: 22px; width: 225px; height: 110px;
    background: linear-gradient(180deg, #3f6fc4 0%, #8fb0e0 55%, #7d6b4c 100%);
  }
  .photo--cabin-panels {
    left: 300px; top: 150px; width: 225px; height: 140px;
    background: linear-gradient(180deg, #2f4d22 0%, #5b4a34 45%, #b34f7a 80%, #3e6a2a 100%);
  }
  .photo--vineyard-array {
    left: 0; top: 540px; width: 550px; height: 200px;
    background: linear-gradient(180deg, #a9c6e6 0%, #e6eef5 35%, #4f7a30 55%, #6d9a3e 80%, #b8c4c8 100%);
  }

  .title-box {
    position: absolute; left: 0; top: 245px; width: 270px; height: 92px;
    background: var(--plum); color: #fff;
    padding: 20px 16px 0 22px;
    font-size: 20px; line-height: 1.18; font-weight: 400;
    white-space: nowrap;
  }
  .label-box {
    position: absolute; left: 330px; top: 470px; width: 220px; height: 62px;
    background: var(--sage); color: #fff;
    display: flex; align-items: center; justify-content: center;
    font-size: 18px; font-weight: 400;
  }

  .copy {
    position: absolute; font-size: 10px; line-height: 1.36;
  }
  .copy p + p { margin-top: 9px; }
  .copy--intro { left: 24px; top: 352px; width: 250px; }
  .copy--thermal { left: 288px; top: 300px; width: 245px; }
  .copy--right-top { left: 28px; top: 24px; width: 250px; }
  .copy--right-mid { left: 28px; top: 305px; width: 280px; }
</style>
</head>
<body>
  <main class="spread">
    <section class="page page--left">
      <div class="photo photo--wine-glasses" role="img" aria-label="Close-up of two glasses of red and white wine against a green vineyard background"></div>
      <h2 class="title-box">Solar Thermal<br>Water Heating Systems</h2>

      <div class="copy copy--intro">
        <p>Wine producers of California are ideally positioned to provide leadership in renewable energy installation. Seldom is there an opportunity presented that has immediate financial benefit, increased operational efficiency and long term customer loyalty development as can now be achieved now by converting to eco-friendly energy producing sources.</p>
        <p>Central California is blessed with abundant amounts of sunlight, temperate climate, and lots of grape vines! All work together to provide wineries and grape growers with numerous opportunities to benefit from a variety of renewable energy resources.</p>
        <p>Your customers expect environmentally conscious practices will be used to produce their favorite wine. Minimal use of energy goes hand-in-hand with organic and natural farming techniques. Wineries that prominently display commitment to ecofriendly operations will benefit from customer goodwill.</p>
        <p>Whether it is production of solar electricity for improving energy efficiency of your customer-facing tasting rooms or for offsetting electrical costs for water pumping, installation of PV solar modules can effectively eliminate the majority of your electrical costs.</p>
      </div>

      <div class="copy copy--thermal">
        <p>Winery barrel-cleaning operations consume large amounts of propane. No problem. Solar hot water heating can be the answer. Recent progress in solar thermal panels has been remarkable. They produce hot water… and lots of it. Modern winery operations can offset as much as 70% of water heating needs using solar thermal systems.</p>
        <p>Environmentally conscious wine club members will soon be arriving at tasting rooms around the wine country. They will have two things on their minds, where is the best wine tasting, and where can I recharge my EV? Forward-thinking businesses that offer electric charging stations will be sure to capture the business, if not the heart, of these visitors. The EV charging costs can be predictably offset by on-site production of solar electricity.</p>
      </div>

      <div class="photo photo--grapes" role="img" aria-label="Cluster of ripe purple wine grapes with vine leaves"></div>
    </section>

    <section class="page page--right">
      <div class="copy copy--right-top">
        <p>Like every system we install, our solar thermal packages are designed and fitted by local crews who live and work in the wine country. We size each array to the real demands of your cellar, your barrel room and your tasting room, so the system pays back quickly and keeps working quietly for decades with very little upkeep.</p>
      </div>

      <div class="photo photo--collector" role="img" aria-label="Dish-shaped solar thermal collector under a blue sky"></div>
      <div class="photo photo--cabin-panels" role="img" aria-label="Wooden winery building with solar panels on the roof behind flowering plants"></div>

      <div class="copy copy--right-mid">
        <p>Solar thermal systems can be among the most cost-effective of all renewable systems. Thermal collectors capture large amounts of energy from the sun and use it to heat water for washing, sanitizing and process needs. Collectors range in size and type, and they can be matched to the volume of hot water your winery uses each day. Modern tracking collectors produce far more hot water from the same roof area than older fixed panels.</p>
      </div>

      <h2 class="label-box">Solar Electric System</h2>
      <div class="photo photo--vineyard-array" role="img" aria-label="Ground-mounted solar panel array beside rolling green vineyard hills and an oak tree"></div>
    </section>
  </main>
</body>
</html>
```